Crash Reapirer business card design

We are a crash repair business based in a small country town in South Australia with our own spray booth. We do all types of repairs for both insurance companies and private jobs. We also replace broken windscreens.
We usually have the KVL logo on our cards because we are KVL approved repairers.
We would also like the JPO (Vehicle Guild Federation)logo because we are a member for them also.
If the card could incorporate black, grey, white and silver colours that would be excellent.
We do not have our own logo if 1 could be created that would be great.

Industry/Entity Type

Insurance

Contact Information for Business Card

Dorvick Crash Repairs
47 Tulloch Ave, Coralby SA 5190
Ph 08 85213077 Fax 08 85213358
Kent 0412658341
Email - dorcrash@fernmail.com

We do private & insurance work, windscreen replacements on all makes & models of cars

```html
<!DOCTYPE html>
<html lang="en">
<head>
<meta charset="utf-8">
<title>Dorvick Crash Repairs – Business Card</title>
<link rel="stylesheet" href="https://fonts.googleapis.com/css2?family=Mulish:wght@400;600;800&display=swap">
<style>
  :root {
    --backdrop: #d9dadc;
    --card-black: #000000;
    --card-white: #ffffff;
    --card-silver: #e4e5e7;
    --accent-blue: #3d7fd1;
    --text-dark: #1a1a1a;
    --text-light: #ffffff;
  }
  * { margin: 0; padding: 0; box-sizing: border-box; }
  html, body {
    width: 1200px;
    height: 960px;
    overflow: hidden;
    background: var(--backdrop);
    font-family: "Mulish", Arial, sans-serif;
  }
  .card {
    position: absolute;
    left: 150px;
    top: 205px;
    width: 900px;
    height: 550px;
    background: linear-gradient(180deg, var(--card-white) 0%, var(--card-silver) 100%);
    box-shadow: 0 14px 40px rgba(0,0,0,0.18);
    overflow: hidden;
  }
  .card__band {
    position: absolute;
    left: 0; top: 0;
    width: 100%;
    height: 330px;
    background: var(--card-black);
  }
  .brand {
    position: absolute;
    right: 60px;
    top: 110px;
    display: flex;
    align-items: center;
    gap: 22px;
  }
  .brand__square {
    width: 64px;
    height: 64px;
    background: var(--accent-blue);
  }
  .brand__name {
    color: var(--text-light);
    font-weight: 800;
    line-height: 0.95;
    text-align: right;
  }
  .brand__name-main { display: block; font-size: 74px; letter-spacing: -1px; }
  .brand__name-sub { display: block; font-size: 40px; margin-top: 6px; }
  .tagline {
    position: absolute;
    left: 36px;
    top: 292px;
    color: var(--text-light);
    font-size: 19px;
    font-weight: 400;
  }
  .address {
    position: absolute;
    left: 40px;
    top: 356px;
    color: var(--text-dark);
    font-size: 21px;
    line-height: 1.5;
  }
  .label { color: var(--accent-blue); }
  .contact {
    position: absolute;
    right: 60px;
    top: 410px;
    text-align: right;
    color: var(--text-dark);
    font-size: 22px;
    line-height: 1.35;
  }
  .contact__name {
    color: var(--accent-blue);
    font-size: 40px;
    font-weight: 400;
    letter-spacing: 1px;
    line-height: 1.1;
  }
</style>
</head>
<body>
  <article class="card">
    <div class="card__band">
      <div class="brand">
        <span class="brand__square" aria-hidden="true"></span>
        <p class="brand__name">
          <span class="brand__name-main">Dorvick</span>
          <span class="brand__name-sub">Crash Repairs</span>
        </p>
      </div>
      <p class="tagline">We do private &amp; insurance work, windscreen replacements on all makes &amp; models of cars</p>
    </div>

    <div class="address">
      <p>Dorvick Crash Repairs</p>
      <p>47 Tulloch Ave, Coralby SA 5190</p>
      <p><span class="label">Ph:</span> 08 85213077 <span class="label">Fax:</span> 08 85213358</p>
    </div>

    <div class="contact">
      <p class="contact__name">KENT</p>
      <p>0412658341</p>
      <p>Email:&nbsp; dorcrash@fernmail.com</p>
    </div>
  </article>
</body>
</html>
```